Business Card Design Project - IT Company

Kestrafield Information Technology Solutions
We are an Information Technology Company. We provide computer services to commercial companies. We would like a new card full color front and back with bleeding edge.
We have a logo that you can use or if you want to come up with a new logo that is fine too.
Our colors are mostly Maroon and black but be creative.
Sample Information
Brent R Okafor
4812 W Saguaro Ridge Drive
Suite 600
Phoenix, AZ 85016
O: 602.914.2037
C: 602.468.1290
24/7: 888.914.2037
bokafor@kestrafield.example
www.kestrafield.example
Target Market(s)
Business of all sizes
Industry/Entity Type
Computer
Requirements
Must have
- Bleeding edge
full color on both sides

```html
<!DOCTYPE html>
<html lang="en">
<head>
<meta charset="utf-8">
<title>Kestrafield Business Card – Front and Back</title>
<link rel="stylesheet" href="https://fonts.googleapis.com/css2?family=Open+Sans:wght@400;600&family=PT+Sans&display=swap">
<style>
  :root {
    --page: #ffffff;
    --maroon: #b3141c;
    --accent-red: #e0141b;
    --ink: #333333;
    --trim-line: #1d1d1d;
    --front-top: #fbfbfc;
    --front-mid: #e4e4ea;
    --back-top: #6b6764;
    --back-bottom: #1b1a19;
    --silver: #e9e9ec;
  }
  * { margin: 0; padding: 0; box-sizing: border-box; }
  html, body { width: 1200px; height: 900px; overflow: hidden; background: var(--page); }
  .sheet { position: relative; width: 1200px; height: 900px; font-family: "Open Sans", sans-serif; }

  /* Front card */
  .card-front {
    position: absolute; left: 180px; top: 92px; width: 541px; height: 324px;
    border: 1.5px solid var(--trim-line);
    background: linear-gradient(180deg, var(--front-top) 0%, var(--front-mid) 55%, var(--front-top) 100%);
  }
  .card-front .trim {
    position: absolute; left: 16px; top: 15px; width: 508px; height: 292px;
    border: 1.5px solid var(--trim-line);
  }
  .front-brand { position: absolute; left: 40px; top: 155px; width: 210px; text-align: center; color: var(--ink); }
  .front-brand .brand-name { font-size: 34px; font-weight: 400; line-height: 1; letter-spacing: -0.5px; }
  .front-brand .brand-tagline { font-size: 11px; margin-top: 7px; }
  .divider {
    position: absolute; left: 279px; top: 62px; width: 2px; height: 196px;
    background: linear-gradient(180deg, rgba(224,20,27,0) 0%, var(--accent-red) 45%, rgba(224,20,27,0) 100%);
  }
  .person-name { position: absolute; left: 331px; top: 78px; font-size: 19px; color: var(--maroon); font-weight: 600; letter-spacing: -0.2px; }
  .contact-list { position: absolute; left: 309px; top: 121px; list-style: none; }
  .contact-list li { display: flex; align-items: flex-start; font-size: 12.5px; line-height: 16.7px; color: var(--ink); }
  .contact-list .icon { width: 13px; height: 13px; margin: 2px 9px 0 0; flex: none; }
  .contact-list .no-icon { width: 22px; flex: none; }

  /* Back card */
  .card-back {
    position: absolute; left: 180px; top: 485px; width: 541px; height: 324px;
    background: linear-gradient(180deg, var(--back-top) 0%, #3e3b39 45%, var(--back-bottom) 100%);
  }
  .card-back .trim {
    position: absolute; left: 17px; top: 17px; width: 507px; height: 289px;
    border: 1.5px solid var(--silver);
  }
  .back-brand { position: absolute; left: 0; top: 142px; width: 541px; text-align: center; color: var(--silver); }
  .back-brand .brand-name { font-size: 60px; font-weight: 400; line-height: 1; letter-spacing: -1px; }
  .back-brand .brand-tagline { font-size: 18px; margin-top: 12px; }

  /* Print annotations */
  .bleed-note { position: absolute; left: 0; width: 1200px; height: 60px; }
  .bleed-note svg { position: absolute; left: 0; top: 0; }
  .bleed-note .label {
    position: absolute; left: 814px; top: 0; font-family: "PT Sans", sans-serif;
    font-size: 23px; line-height: 28px; color: var(--accent-red);
  }
  .note-front { top: 154px; }
  .note-back { top: 531px; }
</style>
</head>
<body>
<div class="sheet">

  <section class="card-front" aria-label="Card front">
    <div class="trim"></div>
    <div class="front-brand">
      <div class="brand-name">Kestrafield</div>
      <div class="brand-tagline">Information Technology Solutions</div>
    </div>
    <div class="divider"></div>
    <h1 class="person-name">Brent R Okafor</h1>
    <ul class="contact-list">
      <li><svg class="icon" viewBox="0 0 13 13"><rect width="13" height="13" rx="2" fill="#b3141c"/><path d="M3 7 L6.5 3.5 L10 7 V10 H3 Z" fill="#fff"/></svg>4812 W Saguaro Ridge Drive</li>
      <li><span class="no-icon"></span>Suite 410, Tempe, AZ 85281</li>
      <li><svg class="icon" viewBox="0 0 13 13"><rect width="13" height="13" rx="2" fill="#b3141c"/><path d="M4 3 L5.5 3 L6 5 L5 6 Q6 8 7.5 8.5 L8.5 7.5 L10 8 V9.5 Q6 10 3.5 5 Z" fill="#fff"/></svg>602.914.2037</li>
      <li><svg class="icon" viewBox="0 0 13 13"><rect width="13" height="13" rx="2" fill="#b3141c"/><rect x="4.5" y="2.5" width="4" height="8" rx="1" fill="#fff"/></svg>602.468.1290</li>
      <li><svg class="icon" viewBox="0 0 13 13"><rect width="13" height="13" rx="2" fill="#b3141c"/><circle cx="6.5" cy="6.5" r="3.5" fill="none" stroke="#fff" stroke-width="1.3"/><path d="M6.5 4.5 V6.5 H8" stroke="#fff" stroke-width="1.2" fill="none"/></svg>888.914.2037</li>
      <li><svg class="icon" viewBox="0 0 13 13"><rect width="13" height="13" rx="2" fill="#b3141c"/><rect x="2.5" y="4" width="8" height="5.5" fill="#fff"/><path d="M2.5 4 L6.5 7 L10.5 4" stroke="#b3141c" stroke-width="0.9" fill="none"/></svg>bokafor@kestrafield.example</li>
      <li><svg class="icon" viewBox="0 0 13 13"><rect width="13" height="13" rx="2" fill="#b3141c"/><circle cx="6.5" cy="6.5" r="3.5" fill="none" stroke="#fff" stroke-width="1.2"/><path d="M3 6.5 H10 M6.5 3 V10" stroke="#fff" stroke-width="0.9"/></svg>www.kestrafield.example</li>
    </ul>
  </section>

  <section class="card-back" aria-label="Card back">
    <div class="trim"></div>
    <div class="back-brand">
      <div class="brand-name">Kestrafield</div>
      <div class="brand-tagline">Information Technology Solutions</div>
    </div>
  </section>

  <div class="bleed-note note-front">
    <svg width="1200" height="60" viewBox="0 0 1200 60">
      <line x1="704" y1="29" x2="885" y2="29" stroke="#e0141b" stroke-width="1.5"/>
      <circle cx="704" cy="29" r="6" fill="#e0141b"/>
    </svg>
    <div class="label">Bleeding Edge<br>3mm Bleed Included</div>
  </div>

  <div class="bleed-note note-back">
    <svg width="1200" height="60" viewBox="0 0 1200 60">
      <line x1="704" y1="28" x2="885" y2="28" stroke="#e0141b" stroke-width="1.5"/>
      <circle cx="704" cy="28" r="6" fill="#e0141b" stroke="#fff" stroke-width="1.5"/>
    </svg>
    <div class="label">Bleeding Edge<br>3mm Bleed Included</div>
  </div>

</div>
</body>
</html>
```